Brightpath Holdings Business Card

Create a two sided, high gloss, quality business card for Brightpath Holdings.

Target Market(s)

People wanting to purchase, scale, and sell businesses.

Industry/Entity Type

Entrepreneurs

Contact Information for Business Card

One line: Dana Corwell, CPA, CMA Another line: Entrepreneur & Investor Another line: Business Ownership Transition Expert Another line: Multi-State Licensed Real Estate Broker Phone 954-BRTPATH (278-7284) Email Dana@Brightpath Holdings.com Website www.Brightpath.com

Requirements
Must have
• Black Card, logo on one side, all other information on the other side including a small logo.
Nice to have
• Possibly add a tagline "Helping entrepreneurs live a life they don't need a vacation from"
Should not have
• There will not be a mailing address on these cards.

```html
<!DOCTYPE html>
<html lang="en">
<head>
<meta charset="UTF-8">
<title>Brightpath Holdings Business Card</title>
<link rel="stylesheet" href="https://fonts.googleapis.com/css2?family=Montserrat:wght@400;500;600;700&display=swap">
<style>
  :root {
    --stage: #d9d4cc;
    --card: #0d0d0d;
    --gold: #d9b24a;
    --gold-soft: #c9a23e;
    --text: #f2f2f2;
    --photo-a: #2a2420;
    --photo-b: #6b5a3e;
  }
  * { margin: 0; padding: 0; box-sizing: border-box; }
  html, body { width: 900px; height: 1200px; overflow: hidden; }
  body {
    background: var(--stage);
    font-family: "Montserrat", Arial, sans-serif;
    position: relative;
  }
  .card {
    position: absolute;
    left: 78px;
    width: 744px;
    height: 445px;
    background: var(--card);
    border-radius: 30px;
    overflow: hidden;
  }
  .card--front { top: 130px; }
  .card--back { top: 638px; }

  .brand {
    position: absolute;
    display: flex;
    align-items: center;
    color: var(--gold);
    font-weight: 600;
    white-space: nowrap;
  }
  .brand__dot {
    border-radius: 50%;
    background: var(--gold);
    flex: none;
  }
  .brand--small { left: 46px; top: 116px; font-size: 28px; line-height: 34px; gap: 12px; }
  .brand--small .brand__dot { width: 22px; height: 22px; }
  .brand--large { left: 0; right: 0; top: 150px; justify-content: center; font-size: 52px; gap: 20px; }
  .brand--large .brand__dot { width: 38px; height: 38px; }

  .person {
    position: absolute;
    left: 46px;
    top: 210px;
    color: var(--text);
  }
  .person__name {
    color: var(--gold);
    font-weight: 700;
    font-size: 24px;
    line-height: 30px;
  }
  .person__creds {
    font-weight: 500;
    font-size: 15px;
    margin-left: 6px;
  }
  .person__role {
    font-size: 16px;
    line-height: 20px;
    font-weight: 400;
  }
  .divider {
    position: absolute;
    left: 46px;
    top: 318px;
    width: 302px;
    height: 2px;
    background: var(--gold-soft);
  }
  .contact {
    position: absolute;
    left: 42px;
    top: 334px;
    list-style: none;
    color: var(--text);
    font-size: 16px;
  }
  .contact__item {
    display: flex;
    align-items: center;
    gap: 11px;
    height: 24px;
  }
  .contact__icon { width: 15px; height: 15px; flex: none; }

  .portrait {
    position: absolute;
    right: 0;
    top: 0;
    width: 318px;
    height: 100%;
    background: radial-gradient(ellipse at 55% 45%, var(--photo-b) 0%, var(--photo-a) 55%, var(--card) 100%);
  }

  .tagline {
    position: absolute;
    left: 0;
    right: 0;
    top: 360px;
    text-align: center;
    color: var(--text);
    font-size: 17px;
  }
</style>
</head>
<body>
  <section class="card card--front">
    <div class="brand brand--small"><span class="brand__dot"></span>Brightpath Holdings</div>

    <div class="person">
      <p class="person__name">Dana Corwell<span class="person__creds">CPA, CMA</span></p>
      <p class="person__role">Entrepreneur &amp; Investor</p>
      <p class="person__role">Business Ownership Transition Expert</p>
      <p class="person__role">Multi-State Licensed Real Estate Broker</p>
    </div>

    <div class="divider"></div>

    <ul class="contact">
      <li class="contact__item">
        <svg class="contact__icon" viewBox="0 0 16 16"><circle cx="8" cy="8" r="8" fill="#d9b24a"/><path d="M5 4.5l1.6-.4.9 2-1 .8a5 5 0 0 0 2.6 2.6l.8-1 2 .9-.4 1.6c-3.8.2-6.7-2.7-6.5-6.5z" fill="#0d0d0d"/></svg>
        954-BRTPATH (278-7284)
      </li>
      <li class="contact__item">
        <svg class="contact__icon" viewBox="0 0 16 16"><circle cx="8" cy="8" r="8" fill="#d9b24a"/><rect x="4" y="5.2" width="8" height="5.6" fill="#0d0d0d"/><path d="M4 5.4l4 3 4-3" stroke="#d9b24a" stroke-width="1" fill="none"/></svg>
        Dana@Brightpath Holdings.com
      </li>
      <li class="contact__item">
        <svg class="contact__icon" viewBox="0 0 16 16"><circle cx="8" cy="8" r="8" fill="#d9b24a"/><circle cx="8" cy="8" r="4" fill="none" stroke="#0d0d0d" stroke-width="1.2"/><path d="M4 8h8M8 4c-2 2.5-2 5.5 0 8M8 4c2 2.5 2 5.5 0 8" stroke="#0d0d0d" stroke-width="1" fill="none"/></svg>
        www.Brightpath.com
      </li>
    </ul>

    <div class="portrait" role="img" aria-label="Portrait photograph of Dana Corwell in a dark blazer and yellow blouse"></div>
  </section>

  <section class="card card--back">
    <div class="brand brand--large"><span class="brand__dot"></span>Brightpath Holdings</div>
    <p class="tagline">Helping entrepreneurs live a life they don't need a vacation from</p>
  </section>
</body>
</html>
```